Web re-design project for web software development agency

We need to re-design our existing website (www.tovenmedia.co.uk), and are going to start using a shorter domain (www.toven.com).
We have been in business for 8 years and it's time for an update.

We are based at Harrowmede Court (home of the code breakers). We specialise in writing software for the web. Over the years we have built up a healthy customer base and it is time to incorporate the features we build for our customers into our own site (e.g. social media).

We have a team of 8 talented developers with varied skills including: apps for mobile; complex server side software; front-end software; eCommerce software; specialised web based applications; integration software; hardware support; consultancy services. Our customers are diverse (e.g. banking; commerce; veterinary; R&D; health sector; law; accounting; film industry etc.).

Our current colour scheme is blue, white and green although we are not averse to moving away from these colours. We will also be dropping the DESIGN from our name and logo. Revised logo will be attached.

The site needs to be modern, sophisticated and leading edge. We want to show visitors to the site that we are a professional organisation.
Updates

Our logo in PSD format has been uploaded. Please drop the word DESIGN from the logo.

The deliverable for this project is a PSD (ideally we would like to see how the home page, portfolio page, resources page with mugshots, and forms are going to look).

Many thanks,
Tom

Please DO NOT include a Careers section 

We will also need a "meet our team" section with spaces for 10 photographs as well as some space underneath them so that we can add a short paragraph for each one of them.

Target Market(s)

Mainly large corporations needing bespoke web software, or generally complex projects (for anyone).

Industry/Entity Type

Software

Requirements
Must have
• We would like a home page designed that has the following elements on it:
- Show the new cookie compliance policy displayed probably in the top of the page (will disappear).
- A client Testimonial.
- Pricing icon.
- Social media Links.
- A Quote section in expand/collapse field as in (http://www.quillbrook-online.co.uk/our-services.shtml)

We would also like a portfolio page that showcases our clients in an interesting way.

Finally, we would like a form design that we can use throughout the site (i.e. how should buttons, radio buttons, checkboxes, dropdowns, text areas etc. look)?
Nice to have
• A page that follows these guidelines:
http://www.pagerivet.com/the-anatomy-of-a-perfect-landing-page

Here are a few examples of sites in our sector that we like:
- http://www.tidewell-studio.com/
- http://plinthos.co.uk/
- http://www.fernaxis.com/services/web-development (nice contact us page)
- http://www.quillbrook-online.co.uk/
- http://www.lumsa.com/
- http://www.netmoxa.co.uk/
Should not have
• No flash elemets. If anything, we will use html5.

```html
<!DOCTYPE html>
<html lang="en">
<head>
<meta charset="utf-8">
<title>Toven – Web Application Development</title>
<link rel="stylesheet" href="https://fonts.googleapis.com/css2?family=PT+Sans:wght@400;700&family=PT+Sans+Narrow:wght@700&family=Arimo:wght@400;700&display=swap">
<style>
:root{
  --blue-dark:#0b4f86;
  --blue-deep:#083f6d;
  --blue-hero:#0a5a92;
  --green:#b5bd2a;
  --green-light:#d4d83a;
  --grey-text:#6f6f6f;
  --grey-title:#595959;
  --body-text:#333;
  --panel:#ececec;
  --white:#fff;
}
*{box-sizing:border-box;margin:0;padding:0}
html,body{width:1072px;height:1200px;overflow:hidden;background:var(--white)}
.canvas{width:1072px;height:1200px;overflow:hidden;position:relative}
.page{position:absolute;left:0;top:0;width:980px;height:1097px;transform:scale(1.0939);transform-origin:0 0;font-family:"Arimo",Arial,sans-serif}
.abs{position:absolute}
.lines{white-space:nowrap}

/* header */
.brand-card{left:16px;top:0;width:336px;height:122px;background:var(--white);box-shadow:0 3px 10px rgba(0,0,0,.3);display:flex;align-items:center;gap:14px;padding-left:30px;z-index:3}
.brand-mark{width:38px;height:38px;background:var(--green)}
.brand-name{font-family:"PT Sans",sans-serif;font-weight:700;font-size:50px;color:var(--blue-dark);letter-spacing:1px}
.search{left:674px;top:12px;width:176px;height:24px;background:#e2e2e2;border-radius:3px 0 0 3px;font-size:12px;color:#444;padding:5px 10px}
.search-btn{left:828px;top:12px;width:22px;height:24px;background:var(--blue-dark)}
.social{left:862px;top:11px;display:flex;gap:3px}
.social span{display:block;width:24px;height:24px;background:var(--blue-dark);border-radius:3px}
.social span:last-child{background:#f08a1d}
.nav{left:413px;top:61px;display:flex;font-family:"PT Sans",sans-serif;font-size:14px}
.nav a{display:block;height:39px;line-height:32px;padding:0 13px;color:var(--blue-dark);text-decoration:none}
.nav a.active{background:var(--green);color:#222;padding:0 11px}

/* hero */
.hero{left:0;top:100px;width:980px;height:322px;background:radial-gradient(ellipse at 45% 35%,#1a74ad 0%,var(--blue-hero) 45%,var(--blue-deep) 100%)}
.hero-title{left:12px;top:152px;font-family:"PT Sans",sans-serif;font-weight:700;font-size:35px;line-height:37px;color:var(--white)}
.hero-title em{font-style:normal;color:var(--green-light)}
.hero-list{left:12px;top:235px;list-style:none;font-family:"PT Sans",sans-serif;font-size:15.5px;line-height:22.5px;color:var(--white)}
.hero-list li{padding-left:19px;position:relative}
.hero-list li::before{content:"";position:absolute;left:0;top:11px;width:8px;height:2px;background:var(--green-light)}
.hero-btn{left:379px;top:336px;width:102px;height:31px;background:linear-gradient(#7fd1d4,#3a9db0);border:1px solid #bfe;font-family:"PT Sans",sans-serif;font-weight:700;font-size:15px;color:#225;text-align:center;line-height:29px}
.hero-visual{left:540px;top:112px;width:432px;height:300px;background:linear-gradient(135deg,rgba(255,255,255,.22),rgba(255,255,255,.06));border-radius:4px}

/* service cards */
.card{top:460px;width:293px;height:337px;background:linear-gradient(#e2e2e2,#f3f3f3 30%,#f6f6f6);border:1px solid #d6d6d6;border-radius:4px}
.card-title{position:absolute;left:13px;top:16px;font-family:"PT Sans Narrow",sans-serif;font-weight:700;font-size:36px;color:var(--grey-title)}
.card-ribbon{position:absolute;left:191px;top:-8px;width:96px;height:94px}
.card-ticks{position:absolute;left:14px;top:59px;list-style:none;font-weight:700;font-size:15px;color:#888;line-height:26px}
.card-ticks li{display:flex;align-items:center;gap:13px}
.card-text{position:absolute;left:14px;top:122px;font-size:12.2px;line-height:20px;color:var(--grey-text);height:120px;overflow:hidden}
.price{position:absolute;left:-9px;top:245px;width:310px;height:76px;background:linear-gradient(var(--green-light),var(--green) 60%,#9aa21c);border-radius:6px;display:flex;align-items:center;justify-content:center;gap:14px;font-family:"PT Sans Narrow",sans-serif;font-weight:700;font-size:29px;color:var(--white)}
.price-go{width:30px;height:30px;border-radius:50%;background:#222;display:flex;align-items:center;justify-content:center}

/* clients */
.clients{left:12px;top:810px;width:595px;height:62px;display:flex;justify-content:space-around;align-items:center;font-family:"PT Sans",sans-serif;font-weight:700;font-size:15px;color:var(--blue-dark)}
.rule{left:12px;top:885px;width:595px;border-top:1px dashed #bbb}

/* welcome */
.section-title{font-weight:700;font-size:17px;color:var(--blue-dark)}
.welcome-text{left:12px;top:920px;font-size:12.2px;line-height:21px;color:var(--body-text)}
.more{font-weight:700;font-size:12.3px;color:var(--blue-dark);display:flex;align-items:center;gap:5px}
.welcome-visual{left:499px;top:922px;width:130px;height:124px;border:4px solid #ddd;background:linear-gradient(135deg,#2a6fc4,#4cb6b0 45%,#f0c23a 70%,#d43a7a)}

/* right column */
.testimonial{left:658px;top:836px;width:310px;height:122px;background:var(--panel);border:1px solid #ccc;padding:11px 0 0 24px;font-size:12.2px;line-height:21px;color:var(--body-text)}
.testimonial cite{display:block;font-style:normal;font-weight:700;color:var(--blue-dark);margin-top:-1px}
.quote-open,.quote-close{position:absolute;font-family:"PT Sans",sans-serif;font-weight:700;font-size:26px;color:#888;line-height:1}
.quote-open{left:9px;top:7px}
.quote-close{left:214px;top:71px}
.news-text{left:667px;top:990px;font-size:12.2px;line-height:21px;color:var(--body-text)}
.news-date{left:667px;top:1034px;font-size:12.3px;font-weight:700;color:#555}

.footer{left:0;top:1063px;width:980px;height:34px;background:#e4e4e4;font-size:12px;color:#444;text-align:center;line-height:34px}
</style>
</head>
<body>
<div class="canvas">
<div class="page">

  <header>
    <div class="abs brand-card"><span class="brand-mark"></span><span class="brand-name">TOVEN</span></div>
    <div class="abs search">Search...</div>
    <div class="abs search-btn"><svg width="22" height="24" viewBox="0 0 22 24"><circle cx="12" cy="10" r="4" fill="none" stroke="#fff" stroke-width="2"/><line x1="9" y1="13" x2="6" y2="17" stroke="#fff" stroke-width="2"/></svg></div>
    <div class="abs social" aria-label="Social links: Chatter, Chirpline, Linkwork, RSS"><span></span><span></span><span></span><span></span></div>
    <nav class="abs nav">
      <a class="active" href="#">Home</a><a href="#">About Us</a><a href="#">Our Services</a><a href="#">Technology</a><a href="#">Portfolio</a><a href="#">Jobs</a><a href="#">Contact Us</a>
    </nav>
  </header>

  <section>
    <div class="abs hero"></div>
    <div class="abs hero-visual" role="img" aria-label="Product photo: desktop computer and mouse showing a client website"></div>
    <h1 class="abs hero-title">Our Speciality : <em>Web application</em><br><em>Development</em> and <em>Support</em></h1>
    <ul class="abs hero-list">
      <li>We can turn your business processes into online web applications.</li>
      <li>We can get your products or services selling online.</li>
      <li>We can convert your site into one that you can maintain yourself.</li>
      <li>We can help ensure your website is usable and standards compliant.</li>
    </ul>
    <div class="abs hero-btn">Read More</div>
  </section>

  <section>
    <div class="abs card" style="left:20px">
      <h2 class="card-title">Design</h2>
      <svg class="card-ribbon" viewBox="0 0 96 94"><path d="M0 0H96V94L48 72L0 94Z" fill="#0b5a93"/><circle cx="48" cy="38" r="20" fill="#f0c54a" role="img" aria-label="Easel icon"/></svg>
      <ul class="card-ticks"><li><svg width="18" height="14"><path d="M1 7l5 5L17 1" stroke="#0b4f86" stroke-width="4" fill="none"/></svg>Graphic Design</li><li><svg width="18" height="14"><path d="M1 7l5 5L17 1" stroke="#0b4f86" stroke-width="4" fill="none"/></svg>Web Design</li></ul>
      <p class="card-text lines">Lorem Ipsum is simply dummy text of the printing<br>and typesetting industry. Lorem Ipsum has been<br>the industry's standard dummy text ever since the<br>1500s, when an unknown printer took a galley of<br>type and scrambled it to make a type specimen<br>book. It has survived not only five centuries, but</p>
      <div class="price">$ 520 <span class="price-go"><svg width="12" height="12"><path d="M3 2l6 4-6 4Z" fill="#b5bd2a"/></svg></span></div>
    </div>
    <div class="abs card" style="left:343px">
      <h2 class="card-title">IT Solutions</h2>
      <svg class="card-ribbon" viewBox="0 0 96 94"><path d="M0 0H96V94L48 72L0 94Z" fill="#0b5a93"/><circle cx="48" cy="38" r="20" fill="#d9dde0" role="img" aria-label="Wrench and screwdriver icon"/></svg>
      <ul class="card-ticks"><li><svg width="18" height="14"><path d="M1 7l5 5L17 1" stroke="#0b4f86" stroke-width="4" fill="none"/></svg>Graphic Design</li><li><svg width="18" height="14"><path d="M1 7l5 5L17 1" stroke="#0b4f86" stroke-width="4" fill="none"/></svg>Web Design</li></ul>
      <p class="card-text lines">Lorem Ipsum is simply dummy text of the printing<br>and typesetting industry. Lorem Ipsum has been<br>the industry's standard dummy text ever since the<br>1500s, when an unknown printer took a galley of<br>type and scrambled it to make a type specimen<br>book. It has survived not only five centuries, but</p>
      <div class="price">$ 410 <span class="price-go"><svg width="12" height="12"><path d="M3 2l6 4-6 4Z" fill="#b5bd2a"/></svg></span></div>
    </div>
    <div class="abs card" style="left:666px">
      <h2 class="card-title">Support</h2>
      <svg class="card-ribbon" viewBox="0 0 96 94"><path d="M0 0H96V94L48 72L0 94Z" fill="#0b5a93"/><circle cx="48" cy="38" r="20" fill="#2a2a2a" role="img" aria-label="Headset icon"/></svg>
      <ul class="card-ticks"><li><svg width="18" height="14"><path d="M1 7l5 5L17 1" stroke="#0b4f86" stroke-width="4" fill="none"/></svg>Graphic Design</li><li><svg width="18" height="14"><path d="M1 7l5 5L17 1" stroke="#0b4f86" stroke-width="4" fill="none"/></svg>Web Design</li></ul>
      <p class="card-text lines">Lorem Ipsum is simply dummy text of the printing<br>and typesetting industry. Lorem Ipsum has been<br>the industry's standard dummy text ever since the<br>1500s, when an unknown printer took a galley of<br>type and scrambled it to make a type specimen<br>book. It has survived not only five centuries, but</p>
      <div class="price">$ 652 <span class="price-go"><svg width="12" height="12"><path d="M3 2l6 4-6 4Z" fill="#b5bd2a"/></svg></span></div>
    </div>
  </section>

  <section>
    <div class="abs clients"><span>Lumaray</span><span>Aurumvault</span><span>Pellaris</span><span>Rattlebox Records</span></div>
    <div class="abs rule"></div>
    <h2 class="abs section-title" style="left:12px;top:896px">Welcome to TOVEN</h2>
    <p class="abs welcome-text lines">Toven Limited was founded in March 2004 and is based at Harrowmede Court<br>in Milton Keynes. The original purpose of the business was to develop websites<br>for any industry. Since then, the company has continued to develop websites,<br>but has specialised in online application systems. The company has also<br>branched out into IT management and support services.</p>
    <div class="abs more" style="left:409px;top:1006px">Read More <svg width="6" height="8"><path d="M0 0l6 4-6 4Z" fill="#0b4f86"/></svg></div>
    <div class="abs welcome-visual" role="img" aria-label="Colourful abstract swirl illustration with stars and butterflies"></div>
  </section>

  <aside>
    <h2 class="abs section-title" style="left:657px;top:808px">Testimonials</h2>
    <blockquote class="abs testimonial lines"><span class="quote-open">“</span>Lorem Ipsum is simply dummy text of the printing<br>and typesetting industry. Lorem Ipsum has been<br>the 1500s, when an unknown printer...<span class="quote-close">”</span><cite>Mr. Lorem Ipsum</cite></blockquote>
    <h2 class="abs section-title" style="left:657px;top:967px">Fresh News</h2>
    <p class="abs news-text lines">Lorem Ipsum is simply dummy text of the printing and<br>typesetting industry. Lorem Ipsum has been the indus-</p>
    <div class="abs news-date">12 Jun 2012</div>
    <div class="abs more" style="left:896px;top:1035px">Read More <svg width="6" height="8"><path d="M0 0l6 4-6 4Z" fill="#0b4f86"/></svg></div>
  </aside>

  <footer class="abs footer">© Toven Ltd. 2012 Registered in England &amp; Wales Number: 07419356.</footer>

</div>
</div>
</body>
</html>
```